Candle Box & Belly Band Design

Design Candle Box for Soy Candles along with a belly band design that can be used on off the shelf coloured boxes. It is for a premium brand of candle - so i want the packaging to reflect this. I have included must haves below.

The candle boxes will be a few different sizes, but for the purpose of the design it would be something like a cube 12 x 12 x 12 cms

The belly band for standard boxes to be something like 5cm wide on a 12 x 12 x 12cms cube box that goes all the way around the top to the bottom - holding the lid on and providing all the relevant information. Example of box with belly band uploaded

Our company Name : Hazel & Pip - our logo is uploaded

Target Market(s)

Premium Candle Buyers

Colors

Designer to choose colors to be used in the design.

Requirements
Must have
• Must have our logo - our logo can be in any colour
• Must state:
• Soy Candle, Hand Poured, Made in Melbourne,
• A space for the fragrance, size and burn time.
• For this project use Lime, Coconut & Elderfllower, 300grams, 50 Hour burn Time

```html
<!DOCTYPE html>
<html lang="en">
<head>
<meta charset="utf-8">
<title>Hazel &amp; Pip – Soy Candle Box</title>
<link href="https://fonts.googleapis.com/css2?family=Kalam:wght@400&family=Open+Sans:wght@400;600&display=swap" rel="stylesheet">
<style>
  :root {
    --backdrop: #a3b4bb;
    --board: #f4f4f4;
    --board-shade: #e6e6e6;
    --side-shade: #d9d9d9;
    --lime: #cdd255;
    --lime-text: #b3be3c;
    --charcoal: #3c3a3b;
    --ink: #2f2f2f;
    --muted: #9a9a9a;
    --white: #ffffff;
  }
  html, body {
    margin: 0;
    width: 1200px;
    height: 1056px;
    overflow: hidden;
    background: var(--backdrop);
  }
  .canvas {
    position: relative;
    width: 1200px;
    height: 1056px;
    display: flex;
    align-items: center;
    justify-content: center;
    gap: 30px;
  }
  .face {
    position: relative;
    flex: none;
    width: 360px;
    height: 360px;
    background: linear-gradient(160deg, var(--white), var(--board) 60%, var(--board-shade));
    box-shadow: 0 14px 32px rgba(40, 60, 70, 0.25);
  }
  .face.side {
    background: linear-gradient(160deg, var(--board), var(--board-shade) 60%, var(--side-shade));
  }

  .brand-name {
    font: 600 15px/1 "Open Sans", sans-serif;
    color: var(--white);
    white-space: nowrap;
  }
  .brand-seal {
    position: absolute;
    left: 50%;
    transform: translateX(-50%);
    border-radius: 50%;
    background: var(--charcoal);
    display: flex;
    align-items: center;
    justify-content: center;
  }
  .side .brand-seal { top: 42px; width: 130px; height: 130px; }
  .lid .brand-seal  { top: 34px; width: 118px; height: 118px; }

  .product-title {
    position: absolute;
    left: 0;
    right: 0;
    display: flex;
    flex-direction: column;
    align-items: center;
    color: var(--ink);
  }
  .product-title .hand-poured {
    font: 400 12px/1 "Open Sans", sans-serif;
    transform: translateX(18px);
    margin-bottom: 2px;
  }
  .product-title .soy-candle {
    font: 400 36px/1 "Kalam", cursive;
  }
  .product-title .origin {
    font: 400 8px/1 "Open Sans", sans-serif;
    letter-spacing: 0.26em;
    margin-top: 2px;
  }
  .side .product-title { top: 196px; }
  .lid .product-title  { top: 176px; }

  .belly-band {
    position: absolute;
    top: 0;
    left: 104px;
    width: 148px;
    height: 168px;
    background: var(--lime);
  }
  .belly-band .brand-name {
    position: absolute;
    top: 92px;
    left: 0;
    right: 0;
    text-align: center;
  }

  .fragrance {
    position: absolute;
    top: 196px;
    left: 0;
    right: 0;
    margin: 0;
    text-align: center;
    font: 400 21px/1 "Kalam", cursive;
    color: var(--lime-text);
  }
  .fragrance .divider {
    display: inline-block;
    width: 2px;
    height: 22px;
    background: var(--lime-text);
    margin: 0 12px;
    vertical-align: -4px;
  }
  .front .product-title { top: 234px; }

  .spec {
    position: absolute;
    bottom: 24px;
    font: 400 10px/1 "Open Sans", sans-serif;
    color: var(--muted);
  }
  .spec.burn-time { left: 14px; }
  .spec.net-weight { right: 14px; }
</style>
</head>
<body>
  <main class="canvas">
    <section class="face side" aria-label="Box side">
      <div class="brand-seal"><span class="brand-name">Hazel &amp; Pip</span></div>
      <div class="product-title">
        <span class="hand-poured">Hand Poured</span>
        <span class="soy-candle">Soy Candle</span>
        <span class="origin">MADE IN MELBOURNE</span>
      </div>
    </section>

    <section class="face lid" aria-label="Box lid">
      <div class="brand-seal"><span class="brand-name">Hazel &amp; Pip</span></div>
      <div class="product-title">
        <span class="hand-poured">Hand Poured</span>
        <span class="soy-candle">Soy Candle</span>
        <span class="origin">MADE IN MELBOURNE</span>
      </div>
    </section>

    <section class="face front" aria-label="Box front">
      <div class="belly-band" aria-label="Belly band"><span class="brand-name">Hazel &amp; Pip</span></div>
      <p class="fragrance">Lime<span class="divider"></span>Elderflower<span class="divider"></span>Coconut</p>
      <div class="product-title">
        <span class="hand-poured">Hand Poured</span>
        <span class="soy-candle">Soy Candle</span>
        <span class="origin">MADE IN MELBOURNE</span>
      </div>
      <span class="spec burn-time">50 hour burn time</span>
      <span class="spec net-weight">300grams</span>
    </section>
  </main>
</body>
</html>
```